Industrial Laundry News Paper Add

We need a color add for 1/4 page newspaper using blue and white. We are an industrial laundry providing linen washing for condo rental companies. We can provide linen rental and wash customer-owned goods

```html
<!DOCTYPE html>
<html lang="en">
<head>
<meta charset="utf-8">
<title>Summit Ridge Services – Industrial Laundry Ad</title>
<link href="https://fonts.googleapis.com/css2?family=Source+Sans+3:wght@400;600;700&display=swap" rel="stylesheet">
<style>
  :root {
    --navy: #1d3c8c;
    --royal: #2d6cc2;
    --deep: #173476;
    --sky: #74b8e8;
    --white: #ffffff;
    --ink: #1f2a44;
    --steel-light: #e9edf1;
    --steel-mid: #b8c1cb;
    --steel-dark: #7d8794;
  }
  * { margin: 0; padding: 0; box-sizing: border-box; }
  html, body { width: 960px; height: 1200px; overflow: hidden; background: var(--white); }
  body { font-family: "Source Sans 3", "Myriad Pro", Arial, sans-serif; }
  .ad { position: relative; width: 960px; height: 1200px; overflow: hidden; background: var(--white); }
  .ad-shapes { position: absolute; inset: 0; }

  .headline {
    position: absolute; top: 548px; left: 0; width: 960px;
    text-align: center; color: var(--white);
    font-weight: 700; font-size: 48px; letter-spacing: 0.5px;
  }
  .intro {
    position: absolute; top: 620px; left: 0; width: 960px;
    text-align: center; color: var(--white);
    font-size: 30px; line-height: 40px; font-weight: 400;
  }
  .service-icons {
    position: absolute; top: 778px; left: 0; width: 960px;
    display: flex; justify-content: center; gap: 54px;
  }
  .service-icon {
    width: 90px; height: 90px; border-radius: 10px;
    background: var(--white); border: 3px solid #c9dcf2;
    display: flex; align-items: center; justify-content: center;
  }
  .service-icon svg { width: 62px; height: 62px; }

  .brand-name {
    position: absolute; top: 1030px; left: 100px; width: 420px;
    color: var(--navy); font-weight: 700; font-size: 48px; line-height: 52px;
    letter-spacing: 1px;
  }
  .contact {
    position: absolute; top: 1030px; right: 60px;
    list-style: none; display: flex; flex-direction: column; gap: 16px;
  }
  .contact-item {
    display: flex; align-items: center; justify-content: flex-end; gap: 12px;
    color: var(--ink); font-weight: 600; font-size: 23px;
  }
  .contact-icon {
    width: 30px; height: 30px; border-radius: 6px; background: var(--navy);
    display: flex; align-items: center; justify-content: center;
  }
  .contact-icon svg { width: 20px; height: 20px; }
</style>
</head>
<body>
<main class="ad">
  <svg class="ad-shapes" width="960" height="1200" viewBox="0 0 960 1200" aria-hidden="false">
    <defs>
      <linearGradient id="machine-tones" x1="0" y1="0" x2="1" y2="0.4">
        <stop offset="0" stop-color="var(--steel-mid)"/>
        <stop offset="0.55" stop-color="var(--steel-light)"/>
        <stop offset="1" stop-color="var(--steel-dark)"/>
      </linearGradient>
      <radialGradient id="band-glow" cx="0.5" cy="0.45" r="0.65">
        <stop offset="0" stop-color="var(--royal)"/>
        <stop offset="1" stop-color="var(--deep)"/>
      </radialGradient>
    </defs>
    <rect class="hero-photo" x="0" y="0" width="960" height="560" fill="url(#machine-tones)" role="img" aria-label="Photo of a row of front-loading industrial washing machines"/>
    <path class="wave-top-accent" d="M0,478 C220,430 520,408 720,428 C840,440 910,420 960,388 L960,1000 L0,1000 Z" fill="var(--sky)"/>
    <path class="blue-band" d="M0,505 C230,456 520,440 720,458 C840,470 910,450 960,420 L960,980 L0,980 Z" fill="url(#band-glow)"/>
    <path class="wave-bottom-accent" d="M0,1000 C200,948 360,930 560,958 C720,982 850,940 960,850 L960,1200 L0,1200 Z" fill="var(--sky)"/>
    <path class="footer-panel" d="M0,1024 C200,972 360,958 560,984 C720,1006 850,964 960,880 L960,1200 L0,1200 Z" fill="var(--white)"/>
  </svg>

  <h1 class="headline">SUMMIT RIDGE SERVICES</h1>
  <p class="intro">We are an industrial laundry providing linen washing<br>for condo rental companies.<br>We can provide linen rental and wash customer-owned goods</p>

  <div class="service-icons">
    <div class="service-icon" aria-label="Condo furnishings">
      <svg viewBox="0 0 62 62" fill="var(--navy)">
        <rect x="14" y="22" width="34" height="4"/>
        <rect x="18" y="26" width="3" height="18"/>
        <rect x="41" y="26" width="3" height="18"/>
        <rect x="4" y="18" width="3" height="26"/>
        <rect x="4" y="32" width="9" height="3"/>
        <rect x="10" y="32" width="3" height="12"/>
        <rect x="55" y="18" width="3" height="26"/>
        <rect x="49" y="32" width="9" height="3"/>
        <rect x="49" y="32" width="3" height="12"/>
      </svg>
    </div>
    <div class="service-icon" aria-label="Folded linens">
      <svg viewBox="0 0 62 62" fill="var(--navy)">
        <path d="M8,40 L30,48 L54,40 L54,46 L30,54 L8,46 Z"/>
        <path d="M8,29 L30,37 L54,29 L54,35 L30,43 L8,35 Z"/>
        <path d="M8,18 L30,10 L54,18 L54,24 L30,32 L8,24 Z"/>
      </svg>
    </div>
    <div class="service-icon" aria-label="Garment on hanger">
      <svg viewBox="0 0 62 62" fill="none" stroke="var(--navy)" stroke-width="3">
        <path d="M27,12 a4,4 0 1 1 4,5 v5"/>
        <path d="M8,32 L31,22 L54,32"/>
        <path d="M16,30 L16,54 L46,54 L46,30" fill="var(--navy)"/>
      </svg>
    </div>
  </div>

  <p class="brand-name">SUMMIT RIDGE<br>SERVICES</p>

  <ul class="contact">
    <li class="contact-item">+1.5550142600
      <span class="contact-icon"><svg viewBox="0 0 20 20" fill="var(--white)"><path d="M5,2 L8,2 L9,6 L7,8 C8,11 9,12 12,13 L14,11 L18,12 L18,15 C18,17 16,18 14,18 C8,17 3,12 2,6 C2,4 3,2 5,2 Z"/></svg></span>
    </li>
    <li class="contact-item">summitridgeservices.com
      <span class="contact-icon"><svg viewBox="0 0 20 20" fill="none" stroke="var(--white)" stroke-width="1.6"><circle cx="10" cy="10" r="7"/><ellipse cx="10" cy="10" rx="3" ry="7"/><path d="M3,10 H17"/></svg></span>
    </li>
    <li class="contact-item">Pine Hollow, CA 90000, USA
      <span class="contact-icon"><svg viewBox="0 0 20 20" fill="var(--white)"><path d="M10,1 C6,1 4,4 4,7 C4,11 10,19 10,19 C10,19 16,11 16,7 C16,4 14,1 10,1 Z M10,5 a2.2,2.2 0 1 1 0,4.4 a2.2,2.2 0 1 1 0,-4.4 Z" fill-rule="evenodd"/></svg></span>
    </li>
  </ul>
</main>
</body>
</html>
```